VelliFilez Website

VelliFiles - Orderly Medical Filez
We need a Web design for a new company called - VelliFilez.
VelliFilez is a Personal Injury and Medical Record Legal Service Outsourcing company. We help Personal Injury Attorneys - with fact based Medical Chronologies and Summaries.

We take Medical Records in disarray and put them in order and summarize them in a chronological order and Update them as needed (if more medical records are added)
Take Releases (for medical records) and work with doctor practices and get the records if needed

Target Market(s)

Personal Injury Attorneys

Industry/Entity Type

Attorney

Number of Pages Required

2 page

Font styles to use
Serif
Sans Serif

Colors

Designer to choose colors to be used in the design.

Requirements
Must have
• Professional Design
• Just need the design for the Home page and Internal pages - I will do the Coding for the pages in html and/or wordpress.
• Don't worry about the content - just need a design.

```html
<!DOCTYPE html>
<html lang="en">
<head>
<meta charset="utf-8">
<title>VelliFilez – Orderly Medical Filez</title>
<link href="https://fonts.googleapis.com/css2?family=Montserrat:wght@400;500;600&family=Open+Sans:wght@400;600;700&display=swap" rel="stylesheet">
<style>
:root{
  --navy:#1a4480;
  --navy-dark:#163d73;
  --charcoal:#333333;
  --ink:#2b2b2b;
  --text:#6b6b6b;
  --grey-band:#ececec;
  --line:#d9d9d9;
  --white:#ffffff;
}
*{box-sizing:border-box;margin:0;padding:0}
html,body{width:1200px;height:2647px;overflow:hidden}
body{font-family:"Open Sans",Arial,sans-serif;color:var(--text);background:var(--white);position:relative}
.heading{font-family:"Montserrat",Arial,sans-serif;font-weight:500}

/* header */
.site-header{position:absolute;top:0;left:0;width:1200px;height:125px}
.brand{position:absolute;left:78px;top:38px;display:flex;align-items:center;gap:14px}
.brand-mark{width:34px;height:34px;border-radius:50%;background:var(--navy)}
.brand-name{font-family:"Montserrat",Arial,sans-serif;font-weight:600;font-size:34px;color:var(--navy);letter-spacing:1px}
.contact-item{position:absolute;top:38px;display:flex;gap:16px;align-items:flex-start}
.contact-item .dot{width:48px;height:48px;border-radius:50%;background:var(--navy);display:flex;align-items:center;justify-content:center}
.contact-item strong{display:block;font-size:19px;color:var(--ink);font-weight:700;line-height:26px}
.contact-item span{font-size:16px;color:var(--text)}
.phone{left:677px}.email{left:896px}

.main-nav{position:absolute;top:125px;left:0;width:1200px;height:52px;background:var(--charcoal)}
.main-nav a{position:absolute;top:15px;color:var(--white);text-decoration:none;font-size:17px}
.nav-cta{position:absolute;right:78px;top:0;width:165px;height:52px;background:var(--navy);color:var(--white);font-family:"Montserrat",Arial,sans-serif;font-size:19px;font-weight:500;display:flex;align-items:center;justify-content:center}

/* hero */
.hero{position:absolute;top:177px;left:0;width:1200px;height:563px;background:linear-gradient(100deg,#5c6773 0%,#7d8893 45%,#a9b1ba 75%,#c7ccd2 100%)}
.hero-text{position:absolute;left:78px;top:206px;width:560px;color:var(--white)}
.hero-text h1{font-size:42px;font-weight:500;margin-bottom:22px}
.hero-text p{font-size:16px;line-height:25px}

/* services */
.section-title{position:absolute;left:0;width:1200px;text-align:center;font-size:38px;color:var(--ink)}
.section-title em{font-style:normal;color:var(--navy)}
.services-photo{position:absolute;left:78px;top:858px;width:427px;height:280px;background:linear-gradient(135deg,#d9d2cc 0%,#a86a55 55%,#7a3a2c 100%)}
.services-intro{position:absolute;left:555px;top:865px;width:560px;font-size:15px;line-height:25px}
.service{position:absolute;left:553px;width:560px;display:flex;gap:30px}
.service .icon{width:62px;height:72px;border:2px solid var(--navy);display:flex;align-items:center;justify-content:center;flex:none}
.service h3{font-size:21px;font-weight:700;color:#444;margin-bottom:6px}
.service p{font-size:15px;line-height:25px;padding-left:4px}

/* welcome */
.welcome{position:absolute;top:1230px;left:0;width:1200px;height:385px;background:var(--grey-band);text-align:center}
.welcome h2{font-size:38px;color:var(--navy);margin-top:44px;margin-bottom:22px}
.welcome p{width:900px;margin:0 auto 14px;font-size:15px;line-height:25px}
.btn{display:inline-block;margin-top:12px;width:176px;height:45px;line-height:45px;background:var(--navy);color:var(--white);font-family:"Montserrat",Arial,sans-serif;font-size:19px;border-radius:3px}

/* blog */
.blog-card{position:absolute;top:1735px;width:322px;height:425px;border:1px solid var(--line)}
.blog-photo{height:220px;position:relative}
.date{position:absolute;left:16px;top:148px;width:72px;height:82px;background:var(--navy);color:var(--white);text-align:center;font-family:"Montserrat",Arial,sans-serif}
.date b{display:block;font-size:30px;font-weight:600;line-height:44px;margin-top:6px}
.date span{font-size:15px}
.blog-body{padding:34px 16px 0}
.blog-body h3{font-size:19px;line-height:31px;color:#444;font-weight:700;margin-bottom:6px}
.blog-body p{font-size:15px;line-height:25px}

/* footer */
.site-footer{position:absolute;top:2262px;left:0;width:1200px;height:323px;background:var(--navy);color:var(--white);text-align:center}
.footer-nav a{position:absolute;top:52px;color:var(--white);text-decoration:none;font-size:16px}
.f-circle{position:absolute;top:134px;width:58px;height:58px;border:2px solid var(--white);border-radius:50%;display:flex;align-items:center;justify-content:center}
.f-text{position:absolute;top:208px;width:320px;font-size:16px;line-height:26px}
.copyright{position:absolute;top:2585px;left:0;width:1200px;height:62px;background:var(--charcoal);color:var(--white);font-size:16px;text-align:center;line-height:62px}
</style>
</head>
<body>

<header class="site-header">
  <div class="brand"><span class="brand-mark"></span><span class="brand-name">VelliFilez</span></div>
  <div class="contact-item phone">
    <div class="dot"><svg width="20" height="20" viewBox="0 0 24 24" fill="#fff"><path d="M6.6 10.8a15 15 0 006.6 6.6l2.2-2.2c.3-.3.7-.4 1-.2 1.1.4 2.3.6 3.6.6.6 0 1 .4 1 1V20c0 .6-.4 1-1 1A17 17 0 013 4c0-.6.4-1 1-1h3.5c.6 0 1 .4 1 1 0 1.3.2 2.5.6 3.6.1.3 0 .7-.2 1z"/></svg></div>
    <div><strong>Phone</strong><span>123 456 7890</span></div>
  </div>
  <div class="contact-item email">
    <div class="dot"><svg width="22" height="18" viewBox="0 0 24 18" fill="none" stroke="#fff" stroke-width="2"><rect x="2" y="2" width="20" height="14" rx="2"/><path d="M2 3l10 7 10-7"/></svg></div>
    <div><strong>Email</strong><span>info@vellifilez.com</span></div>
  </div>
</header>

<nav class="main-nav">
  <a href="#" style="left:78px">Home</a>
  <a href="#" style="left:175px">About</a>
  <a href="#" style="left:272px">Services</a>
  <a href="#" style="left:385px">News</a>
  <a href="#" style="left:478px">Contact</a>
  <div class="nav-cta">CONTACT US</div>
</nav>

<section class="hero" role="img" aria-label="Doctor with stethoscope typing on a laptop keyboard">
  <div class="hero-text">
    <h1 class="heading">Orderly Medical Filez</h1>
    <p>Lorem Ipsum is simply dummy text of the printing and typesetting industry. Lorem Ipsum has been the industry's standard dummy text ever since the 1500s, when an unknown printer took a galley of type.</p>
  </div>
</section>

<h2 class="section-title heading" style="top:782px">Our <em>Services</em></h2>
<div class="services-photo" role="img" aria-label="Scales of justice statue on a desk beside a person writing"></div>
<p class="services-intro">Lorem Ipsum is simply dummy text of the printing and typesetting industry. Lorem Ipsum has been the industry's standard dummy text ever since the.</p>
<div class="service" style="top:945px">
  <div class="icon"><svg width="34" height="40" viewBox="0 0 34 40" fill="var(--navy)"><circle cx="17" cy="9" r="7"/><path d="M3 38c0-10 6-16 14-16s14 6 14 16z"/><circle cx="22" cy="30" r="3" fill="#fff"/></svg></div>
  <div><h3>Personal injury</h3><p>Lorem Ipsum is simply dummy text of the printing and typesetting industry. Lorem Ipsum has been the industry's.</p></div>
</div>
<div class="service" style="top:1045px">
  <div class="icon"><svg width="40" height="34" viewBox="0 0 40 34" fill="none" stroke="var(--navy)" stroke-width="2.5"><path d="M2 6h12l4 4h20v22H2z"/><path d="M20 15v12M14 21h12"/></svg></div>
  <div><h3>Medical Records Legal Service</h3><p>Lorem Ipsum is simply dummy text of the printing and typesetting industry. Lorem Ipsum has been the industry's.</p></div>
</div>

<section class="welcome">
  <h2 class="heading">Welcome to VELLIFILEZ</h2>
  <p>Lorem Ipsum is simply dummy text of the printing and typesetting industry. Lorem Ipsum has been the industry's standard dummy text ever since the 1500s, when an unknown printer took a galley of type and scrambled it to make a type specimen book. It has survived not only five centuries, but also the leap into electronic typesetting.</p>
  <p>Lorem Ipsum is simply dummy text of the printing and typesetting industry. Lorem Ipsum has been the industry's standard dummy text ever since the 1500s, when an unknown printer took a galley of type and scrambled it to make a type.</p>
  <span class="btn">KNOW MORE</span>
</section>

<h2 class="section-title heading" style="top:1662px;color:var(--navy)">Latest Blog</h2>

<article class="blog-card" style="left:77px">
  <div class="blog-photo" role="img" aria-label="Business handshake over a desk" style="background:linear-gradient(135deg,#cfc6b8,#5a5048 60%,#1f1f1f)"><div class="date"><b>17</b><span>MAY</span></div></div>
  <div class="blog-body"><h3>Lorem Ipsum is simply dummy text of the printing.</h3><p>Lorem Ipsum is simply dummy text of the printing and typesetting industry. Lorem Ipsum has been the industry's.</p></div>
</article>
<article class="blog-card" style="left:438px">
  <div class="blog-photo" role="img" aria-label="Scales of justice on a desk with laptop" style="background:linear-gradient(135deg,#ddd6d0,#a86a55 55%,#6e3426)"><div class="date"><b>17</b><span>MAY</span></div></div>
  <div class="blog-body"><h3>Lorem Ipsum is simply dummy text of the printing.</h3><p>Lorem Ipsum is simply dummy text of the printing and typesetting industry. Lorem Ipsum has been the industry's.</p></div>
</article>
<article class="blog-card" style="left:799px">
  <div class="blog-photo" role="img" aria-label="Medical professional using a smartphone" style="background:linear-gradient(135deg,#9fb8d2,#dfe6ee 55%,#f4f5f7)"><div class="date"><b>17</b><span>MAY</span></div></div>
  <div class="blog-body"><h3>Lorem Ipsum is simply dummy text of the printing.</h3><p>Lorem Ipsum is simply dummy text of the printing and typesetting industry. Lorem Ipsum has been the industry's.</p></div>
</article>

<footer class="site-footer">
  <nav class="footer-nav">
    <a href="#" style="left:380px">Home</a>
    <a href="#" style="left:472px">About</a>
    <a href="#" style="left:565px">Services</a>
    <a href="#" style="left:675px">News</a>
    <a href="#" style="left:763px">Contact</a>
  </nav>
  <svg style="position:absolute;left:410px;top:150px" width="400" height="30" viewBox="0 0 400 30" fill="none" stroke="#fff" stroke-width="1.5">
    <circle cx="5" cy="5" r="4"/><path d="M9 5h300"/><path d="M90 22h300"/><circle cx="385" cy="22" r="4"/>
  </svg>
  <div class="f-circle" style="left:275px"><svg width="20" height="20" viewBox="0 0 24 24" fill="#fff"><path d="M6.6 10.8a15 15 0 006.6 6.6l2.2-2.2c.3-.3.7-.4 1-.2 1.1.4 2.3.6 3.6.6.6 0 1 .4 1 1V20c0 .6-.4 1-1 1A17 17 0 013 4c0-.6.4-1 1-1h3.5c.6 0 1 .4 1 1 0 1.3.2 2.5.6 3.6.1.3 0 .7-.2 1z"/></svg></div>
  <div class="f-circle" style="left:575px;background:var(--navy-dark)"><svg width="18" height="24" viewBox="0 0 18 24" fill="#fff"><path d="M9 0a9 9 0 019 9c0 7-9 15-9 15S0 16 0 9a9 9 0 019-9z"/><circle cx="9" cy="9" r="3.5" fill="var(--navy)"/></svg></div>
  <div class="f-circle" style="left:877px"><svg width="20" height="16" viewBox="0 0 24 18" fill="none" stroke="#fff" stroke-width="2"><rect x="2" y="2" width="20" height="14" rx="2"/><path d="M2 3l10 7 10-7"/></svg></div>
  <div class="f-text" style="left:144px">123 456 7890</div>
  <div class="f-text" style="left:440px">Lorem ipsum dolor sit amet,<br>consectetur adipiscing elit.</div>
  <div class="f-text" style="left:746px">info@vellifilez.com</div>
</footer>
<div class="copyright">©VELLIFILEZ- 2018. All Rights Reserved.</div>

</body>
</html>
```